Following list to be designed:

1. A4 Letter Head

Must comprise of:
BRIGHT HARBOR and its LOGO
Address: No.41, 2F, Tarwin Plaza, Melrick Road, Upper Fenwood Gardens, Bangalore 560 017
Tel: 080 27481930
Fax: 080 27481931
Mail: query@brightharbor.example

Color of wordings to be in the lighter shade of blue and brighter shade of blue.

2. A4 Envelope

Must comprise of:
BRIGHT HARBOR and its LOGO
Tel: 080 27481930
Fax: 080 27481931

3. Postal Envelope

Must comprise of:
BRIGHT HARBOR and its LOGO
Tel: 080 27481930
Fax: 080 27481931

4. Business Card

Must comprise of:
Rohan Mehta
Managing Partner
Cell: +91 9487215043
Mail: rohanmehta@brightharbor.example
Tel: 080 27481930
Fax: 080 27481931

5. A4 Letter Head

Must comprise of:
BRIGHT HARBOR CORP. (wording) and BRIGHT HARBOR LOGO (only blue ribbon)

Blue ribbon (BRIGHT HARBOR LOGO) may be placed on Left Top Corner of the A4 Letter Head
and BRIGHT HARBOR CORP. (wording) to be placed on Right Top Corner of the A4 Letter Head

Tel: 080 27481930
Fax: 080 27481931

6. . A4 Envelope

Must comprise of:

Blue ribbon (BRIGHT HARBOR LOGO) may be placed on Left Top Corner of the A4 Envelope
and BRIGHT HARBOR CORP. (wording) to be placed on Right Top Corner of the A4 Envelope
Tel: 080 27481930
Fax: 080 27481931

Target Market(s)

Top IT/ITES Organizations

Industry/Entity Type

Real Estate Development

Font styles to use
Serif
Sans Serif

Colors
33a6d7
0792cd
85cae6

Requirements
Should not have
• Playful font and color

```html
<!DOCTYPE html>
<html lang="en">
<head>
<meta charset="utf-8">
<title>Bright Harbor — A4 Letterhead</title>
<link href="https://fonts.googleapis.com/css2?family=PT+Sans+Narrow:wght@400;700&display=swap" rel="stylesheet">
<style>
  :root {
    --backdrop: #e9eef2;
    --paper: #ffffff;
    --paper-tint: #eef6fc;
    --brand-blue: #0792cd;
    --brand-blue-mid: #33a6d7;
    --brand-blue-light: #85cae6;
    --band-grey: #a9abad;
    --text-grey: #4a4a4a;
  }
  * { box-sizing: border-box; margin: 0; padding: 0; }
  html, body {
    width: 1200px; height: 784px; overflow: hidden;
    background: var(--backdrop);
    font-family: "PT Sans Narrow", "Arial Narrow", sans-serif;
  }
  .letterhead {
    position: absolute;
    left: 338px; top: 22px;
    width: 524px; height: 740px;
    overflow: hidden;
    background: linear-gradient(20deg, var(--paper-tint) 0%, var(--paper) 40%);
    box-shadow: 0 4px 18px rgba(0,0,0,0.12);
  }
  .brand {
    position: absolute;
    top: 46px; right: 44px;
    display: flex; align-items: center; gap: 8px;
  }
  .brand-dot {
    width: 18px; height: 18px; border-radius: 50%;
    background: var(--brand-blue-mid);
  }
  .brand-name {
    font-weight: 700; font-size: 19px; letter-spacing: 1px;
    color: var(--text-grey);
  }
  .contact-line {
    position: absolute;
    left: 22px; right: 22px; bottom: 20px;
    display: flex; align-items: center; justify-content: space-between;
    flex-wrap: nowrap;
    font-size: 8px; line-height: 1; color: var(--text-grey); white-space: nowrap;
  }
  .contact-group { display: flex; align-items: center; gap: 3px; }
  .contact-icon { width: 8px; height: 8px; flex: none; }
  .footer-band {
    position: absolute; left: 0; right: 0; bottom: 0; height: 6px;
    display: flex;
  }
  .band-blue { flex: 30; background: var(--brand-blue); }
  .band-grey { flex: 31; background: linear-gradient(var(--band-grey), #d6d7d8); }
  .band-blue-end { flex: 39; background: var(--brand-blue-mid); }
</style>
</head>
<body>
  <main class="letterhead">
    <header class="brand">
      <span class="brand-dot"></span>
      <span class="brand-name">BRIGHT HARBOR</span>
    </header>

    <footer class="contact-line">
      <span class="contact-group">
        <svg class="contact-icon" viewBox="0 0 10 10" aria-hidden="true"><circle cx="5" cy="5" r="4.6" fill="var(--brand-blue)"/><path d="M5 2.2a1.8 1.8 0 0 0-1.8 1.8c0 1.4 1.8 3.6 1.8 3.6s1.8-2.2 1.8-3.6A1.8 1.8 0 0 0 5 2.2z" fill="#fff"/></svg>
        <span>No.41, 2F, Tarwin Plaza, Melrick Road, Upper Fenwood Gardens, Bangalore 560 017</span>
      </span>
      <span class="contact-group">
        <svg class="contact-icon" viewBox="0 0 10 10" aria-hidden="true"><circle cx="5" cy="5" r="4.6" fill="var(--brand-blue)"/><path d="M3.3 2.6l1 1-.5.7c.4.8.9 1.3 1.7 1.7l.7-.5 1 1-.6.8C4.8 7.1 2.9 5.2 2.7 3.2z" fill="#fff"/></svg>
        <span>080 27481930</span>
      </span>
      <span class="contact-group">
        <svg class="contact-icon" viewBox="0 0 10 10" aria-hidden="true"><circle cx="5" cy="5" r="4.6" fill="var(--brand-blue)"/><rect x="2.8" y="3.6" width="4.4" height="3" fill="#fff"/><rect x="3.6" y="2.5" width="2.8" height="1.4" fill="#fff"/></svg>
        <span>080 27481931</span>
      </span>
      <span class="contact-group">
        <svg class="contact-icon" viewBox="0 0 10 10" aria-hidden="true"><circle cx="5" cy="5" r="4.6" fill="var(--brand-blue)"/><rect x="2.7" y="3.3" width="4.6" height="3.4" fill="#fff"/><path d="M2.7 3.3L5 5.2l2.3-1.9" fill="none" stroke="var(--brand-blue)" stroke-width=".6"/></svg>
        <span>query@brightharbor.example</span>
      </span>
    </footer>

    <div class="footer-band">
      <span class="band-blue"></span>
      <span class="band-grey"></span>
      <span class="band-blue-end"></span>
    </div>
  </main>
</body>
</html>
```